Billboard design - consider what a billboard is

Design a billboard using my logo - Billboard is 6m x 3m
A Billboard is advertising for my company that is on a big sign.

Has to be clean and easy to read, and ideally highlights that we are Residential and Commercial builders.

Keep it clean and easy to read

The contact number for the board is

022 583 7092
www.harbourframeworks.co.nz
info@harbourframeworks.co.nz

Doesnt have to have all contact details if it doesnt fit

Has to catch peoples attention to contact us if they need a builder

Can you please change the sign to be all white writing, with black background ?
Updates

Please consider what a billboard is...

The design needs to be suitable for a billboard..

Target Market(s)

people driving past

Industry/Entity Type

Construction

Logo Text

Wellington Builder, website email address, contact number

Colors
0054AA
0677BA
7BADD7
CADEEF
E8F1F8

Requirements
Must have
• Easy to read
Nice to have
• easy to read, can clearly see contact details

```html
<!DOCTYPE html>
<html lang="en">
<head>
<meta charset="utf-8">
<title>Harbour Frameworks – Wellington Builder Billboard</title>
<link rel="stylesheet" href="https://fonts.googleapis.com/css2?family=Montserrat:wght@500;600&family=Russo+One&display=swap">
<style>
  :root {
    --board-black: #000000;
    --type-white: #ffffff;
    --band-blue: #0054aa;
    --accent-blue: #0677ba;
  }
  * { margin: 0; padding: 0; box-sizing: border-box; }
  html, body {
    width: 1200px;
    height: 600px;
    overflow: hidden;
    background: var(--board-black);
  }
  .billboard {
    display: block;
    width: 1200px;
    height: 600px;
  }
  .board-bg { fill: var(--board-black); }
  .contact-band { fill: var(--band-blue); }
  .brand-mark { fill: var(--accent-blue); }
  .brand-name,
  .contact-line {
    font-family: "Montserrat", sans-serif;
    font-weight: 500;
    fill: var(--type-white);
  }
  .headline {
    font-family: "Russo One", sans-serif;
    fill: var(--type-white);
  }
</style>
</head>
<body>
  <svg class="billboard" viewBox="0 0 1200 600" role="img" aria-label="Harbour Frameworks – Wellington Builder, residental and commercial. Phone 022 583 7092, www.harbourframeworks.co.nz, info@harbourframeworks.co.nz">
    <rect class="board-bg" x="0" y="0" width="1200" height="600"/>

    <g class="brand">
      <rect class="brand-mark" x="404" y="96" width="40" height="40"/>
      <text class="brand-name" x="460" y="132" font-size="44" textLength="336" lengthAdjust="spacingAndGlyphs">Harbour Frameworks</text>
    </g>

    <text class="headline headline-city" x="196" y="300" font-size="100" textLength="808" lengthAdjust="spacingAndGlyphs">WELLINGTON</text>
    <text class="headline headline-trade" x="317" y="378" font-size="84" textLength="566" lengthAdjust="spacingAndGlyphs">BUILDER</text>
    <text class="headline headline-sectors" x="177" y="418" font-size="30" textLength="846" lengthAdjust="spacing">RESIDENTAL AND COMMERCIAL</text>

    <text class="contact-line email" x="293" y="452" font-size="34" textLength="614" lengthAdjust="spacingAndGlyphs">info@harbourframeworks.co.nz</text>

    <rect class="contact-band" x="0" y="471" width="1200" height="129"/>
    <text class="contact-line phone" x="29" y="554" font-size="56" textLength="353" lengthAdjust="spacingAndGlyphs">022 583 7092</text>
    <text class="contact-line website" x="418" y="548" font-size="46" textLength="752" lengthAdjust="spacingAndGlyphs">www.harbourframeworks.co.nz</text>
  </svg>
</body>
</html>
```